Webdesign for a Bikeshop in Innsbruck (female audience)

To obtain my master's degree, I am conducting a study in the field of web design as part of my master thesis. All submitted designs will therefore be used for study purposes. In order to achieve a homogeneous group, I would like to encourage not only male but also female web designers to submit a design. All submitted designs will be used anonymously for the study and therefore do not allow any conclusions to be drawn about your person. Since this is a contest, the winner will be chosen randomly from all serious submissions. I would be really happy if you would support me in my study. I think the results could be very informative and also useful for your further work (I won't go into more detail here as it could skew the results - but once the contest is over, feel free to contact me. Of course I will also provide you with my results as soon as my work is finished). Below you will find a fictitious usecase and a description of what the website should include:

The company Bikeshop Valdorna is planning to relaunch its own website and would like to present itself primarily as a competent and leading consultant in the field of cargo bikes. The design should appeal to a broad audience and embody an urban lifestyle. In any case, the website should include a landing page, a product overview page and a product details page. The company also wants to appeal mainly to a FEMALE target group. You only design the website. So don't worry about hardware or software limitations, just create the best bike store design you can.

As it is fictitious, I can't offer any materials. A logo is not necessary, you can use a placeholder or whatever you have access to. If you need any inspring websites feel free to contact me.

Target Market(s)

female users

Number of Pages Required

1 page

Requirements
Must have
• landing page, product overview page, product details page
Should not have
• online shop

```html
<!DOCTYPE html>
<html lang="en">
<head>
<meta charset="utf-8">
<title>Bikeshop Valdorna</title>
<link href="https://fonts.googleapis.com/css2?family=Playfair+Display:wght@400;700;900&family=Josefin+Sans:wght@400;600&family=Roboto:wght@400;500&family=Poppins:wght@500;600&display=swap" rel="stylesheet">
<style>
:root{
  --green:#a3c05a;
  --teal:#7aa3a8;
  --teal-dark:#5b7478;
  --ink:#1e1e1e;
  --footer:#2b2f31;
  --white:#ffffff;
  --muted:#444;
}
*{margin:0;padding:0;box-sizing:border-box}
html,body{width:1200px;height:2802px;overflow:hidden;background:var(--white)}
body{position:relative;font-family:'Roboto',sans-serif;color:var(--ink)}
.abs{position:absolute}
.serif{font-family:'Playfair Display',serif}

/* hero */
.hero{left:0;top:0;width:1200px;height:738px;background:linear-gradient(100deg,#6f7378 0%,#8a8a90 45%,#9d8f93 75%,#a49a98 100%)}
.hero-photo{left:0;top:0;width:1200px;height:738px;background:
  radial-gradient(ellipse 500px 260px at 500px 700px,#2f3a2a 0%,transparent 70%),
  linear-gradient(180deg,transparent 60%,#5e7a3d 100%)}
.brand{left:97px;top:26px;font-size:27px;font-weight:700;color:var(--white)}
.nav{left:400px;top:30px;display:flex;gap:46px;font-size:19px;color:var(--white)}
.nav-divider{left:978px;top:26px;width:1px;height:32px;background:#ddd}
.icon-btn{top:29px;width:34px;height:34px;border-radius:50%;display:flex;align-items:center;justify-content:center}
.welcome{left:558px;top:136px;font-family:'Josefin Sans',sans-serif;font-size:35px;font-weight:600;color:var(--white);letter-spacing:1px}
.hero-title{left:558px;top:190px;font-size:72px;font-weight:900;line-height:76px;color:var(--white)}
.pill{background:var(--green);color:var(--white);border-radius:30px;display:flex;align-items:center;justify-content:center;font-family:'Playfair Display',serif;font-weight:700}
.buy{left:561px;top:367px;width:177px;height:52px;font-size:20px}

/* products */
.card-sheet{left:68px;top:672px;width:1063px;height:120px;background:var(--white);border-radius:30px 30px 0 0}
.accent{height:4px;width:54px;background:var(--green)}
.section-title{left:0;top:725px;width:1200px;text-align:center;font-size:31px;font-weight:700}
.product{top:804px;width:228px;height:225px;border-radius:6px;border:3px solid #fff;box-shadow:0 0 8px rgba(0,0,0,.25)}
.p-name{top:1049px;width:228px;text-align:center;font-family:'Playfair Display',serif;font-size:12px;font-weight:700}
.p-price{top:1082px;width:228px;text-align:center;font-family:'Poppins',sans-serif;font-size:15px;font-weight:600}
.view-all{left:492px;top:1152px;width:217px;height:54px;font-size:19px}

/* about */
.about{left:0;top:1269px;width:1200px;height:569px;background:linear-gradient(90deg,var(--teal) 0%,var(--teal) 40%,#8fa890 62%,#a8b57e 80%,#9aa377 100%)}
.about-panel{left:79px;top:1402px;width:510px;height:305px;background:var(--teal-dark);opacity:.92;border-radius:20px}
.about-title{left:106px;top:1430px;font-size:35px;font-weight:700;color:var(--white)}
.about-text{left:107px;top:1497px;width:450px;font-size:16px;line-height:26px;color:var(--white)}
.read-more{left:106px;top:1626px;width:176px;height:53px;font-size:20px}

/* detail */
.detail-img{left:99px;top:1918px;width:496px;height:455px;border-radius:12px;background:linear-gradient(180deg,#c9a37c 0%,#b85a6a 25%,#3da0bd 55%,#a86e5a 100%)}
.d-title{left:632px;top:1948px;font-size:32px;font-weight:400}
.stars{left:632px;top:2001px;display:flex;align-items:center;gap:3px;font-size:15px}
.d-price{left:632px;top:2030px;font-family:'Roboto',sans-serif;font-size:24px;font-weight:500;color:var(--green)}
.d-desc{left:632px;top:2077px;width:470px;font-size:16px;line-height:26px;color:var(--muted)}
.size{left:632px;top:2171px;font-size:20px;font-weight:500}
.size span{font-size:15px;font-weight:400;margin-left:6px}
.opt{top:2221px;height:38px;display:flex;align-items:center;justify-content:center;font-size:15px;border-radius:3px}
.select{left:825px;top:2222px;width:274px;height:36px;border:1px solid #ccc;font-size:14px;display:flex;align-items:center;justify-content:space-between;padding:0 14px 0 11px}
.cart{left:667px;top:2287px;width:361px;height:48px;background:var(--green);color:var(--white);display:flex;align-items:center;justify-content:center;font-weight:500;font-size:16px}
.ship{left:667px;top:2342px;width:361px;text-align:center;font-size:13px}

/* footer */
.footer{left:0;top:2430px;width:1200px;height:372px;background:var(--footer);color:var(--white)}
.f-head{top:2484px;font-size:27px;font-weight:700}
.f-text{font-size:20px;line-height:29px}
.social{top:2656px;width:43px;height:43px;border:2px solid #fff;border-radius:50%}
.contact-ico{width:38px;height:38px;border-radius:50%;background:#fff;display:flex;align-items:center;justify-content:center}
.links{left:898px;top:2550px;font-size:19px;line-height:30px}
.copy{left:0;top:2740px;width:1200px;text-align:center;font-size:18px;font-weight:700}
</style>
</head>
<body>

<div class="abs hero"></div>
<div class="abs hero-photo" role="img" aria-label="Photo of a smiling woman riding a cargo bike with two children in the front box"></div>
<div class="abs brand serif">Bikeshop Valdorna</div>
<nav class="abs nav serif"><span>Home</span><span>About Us</span><span>Products</span><span>Gallery</span><span>Contact Us</span></nav>
<div class="abs nav-divider"></div>
<div class="abs icon-btn" style="left:1005px;background:#ddd">
  <svg width="16" height="16" viewBox="0 0 16 16"><circle cx="6.5" cy="6.5" r="4.5" fill="none" stroke="#222" stroke-width="2"/><line x1="10" y1="10" x2="14" y2="14" stroke="#222" stroke-width="2.4"/></svg>
</div>
<div class="abs icon-btn" style="left:1049px;background:var(--green)">
  <svg width="18" height="16" viewBox="0 0 18 16"><path d="M1 2h3l2 8h9l2-6H5" fill="none" stroke="#fff" stroke-width="2"/><circle cx="7" cy="13.5" r="1.5" fill="#fff"/><circle cx="14" cy="13.5" r="1.5" fill="#fff"/></svg>
</div>
<div class="abs welcome">Welcome to</div>
<div class="abs hero-title serif">BIKESHOP<br>VALDORNA</div>
<div class="abs pill buy">Buy Now</div>

<div class="abs card-sheet"></div>
<div class="abs accent" style="left:573px;top:712px"></div>
<h2 class="abs section-title serif">OUR PRODUCTS</h2>

<div class="abs product" style="left:102px;background:linear-gradient(160deg,#d98a4a,#b86a35 60%,#555)" role="img" aria-label="Row of wooden cargo bikes"></div>
<div class="abs product" style="left:358px;background:#7fa5a9;display:flex;align-items:center;justify-content:center" role="img" aria-label="Cargo bike with cart overlay">
  <svg width="38" height="32" viewBox="0 0 18 16"><path d="M1 2h3l2 8h9l2-6H5z" fill="#fff" stroke="#fff" stroke-width="1.5"/><circle cx="7" cy="13.5" r="1.6" fill="#fff"/><circle cx="14" cy="13.5" r="1.6" fill="#fff"/></svg>
</div>
<div class="abs product" style="left:614px;background:linear-gradient(180deg,#8a5a4a,#d24a1e 55%,#6a6a6a)" role="img" aria-label="Orange box cargo bike parked by a brick wall"></div>
<div class="abs product" style="left:870px;background:linear-gradient(180deg,#a08070,#e0a040 60%,#3a3a3a)" role="img" aria-label="Mother with two children in a cargo bike"></div>

<div class="abs p-name" style="left:102px">CARGO BIKES</div>
<div class="abs p-name" style="left:358px">CARGO BIKES</div>
<div class="abs p-name" style="left:614px">CARGO BIKES</div>
<div class="abs p-name" style="left:870px">CARGO BIKES</div>
<div class="abs p-price" style="left:102px">$39.95Price</div>
<div class="abs p-price" style="left:358px">$39.95Price</div>
<div class="abs p-price" style="left:614px">$79.95Price</div>
<div class="abs p-price" style="left:870px">$39.95Price</div>
<div class="abs pill view-all">Viwe All Products</div>

<div class="abs about" role="img" aria-label="Woman riding a grey cargo bike on a park path at sunset"></div>
<div class="abs about-panel"></div>
<div class="abs accent" style="left:109px;top:1423px;width:62px"></div>
<h2 class="abs about-title serif">About Us</h2>
<p class="abs about-text">Lorem ipsum dolor sit amet, consectetur adipiscing elit, sed do eiusmod tempor incididunt ut labore et dolore magna aliqua. Ut enim ad minim veniam, quis nostrud exercitation ullamco laboris nisi ut aliquip ex ea commodo consequat.</p>
<div class="abs pill read-more">Read More</div>

<div class="abs detail-img" role="img" aria-label="Turquoise cargo bike filled with colourful flowers"></div>
<h2 class="abs d-title serif">CARGO BIKES</h2>
<div class="abs stars">
  <svg width="88" height="16" viewBox="0 0 88 16" fill="#e8552b">
    <path id="st" d="M8 1l2.1 4.6 5 .5-3.8 3.3 1.1 4.9L8 11.8 3.6 14.3l1.1-4.9L.9 6.1l5-.5z"/>
    <use href="#st" x="18"/><use href="#st" x="36"/><use href="#st" x="54"/>
    <use href="#st" x="72" fill="none" stroke="#e8552b" stroke-width="1"/>
  </svg>
  <span>412 Reviews</span>
</div>
<div class="abs d-price">$853.00</div>
<p class="abs d-desc">Lorem ipsum dolor sit amet, consectetur adipiscing elit, sed do eiusmod tempor incididunt ut labore et dolore magna aliqua. Ut enim ad minim veniam</p>
<div class="abs size">Size:<span>Cargo bikes</span></div>
<div class="abs opt" style="left:634px;width:72px;background:#2b2f31;color:#fff">Regular</div>
<div class="abs opt" style="left:722px;width:72px;border:1px solid #6a8ac0;color:#4a6aaa">Large</div>
<div class="abs select"><span>Which Vehicles Will You Needt?</span>
  <svg width="10" height="6" viewBox="0 0 10 6"><path d="M1 1l4 4 4-4" fill="none" stroke="#555" stroke-width="1.4"/></svg>
</div>
<div class="abs cart">ADD TO CART</div>
<div class="abs ship">3-4 day shipping available!</div>

<footer class="abs footer"></footer>
<h3 class="abs f-head serif" style="left:101px;color:#fff">Bikeshop Valdorna</h3>
<p class="abs f-text" style="left:101px;top:2533px;width:270px;color:#fff">Duis aute irure dolor in reprehenderit in voluptate velit esse</p>
<div class="abs social" style="left:101px"></div>
<div class="abs social" style="left:162px"></div>
<div class="abs social" style="left:224px"></div>

<h3 class="abs f-head serif" style="left:500px;color:#fff">Contact Us</h3>
<div class="abs contact-ico" style="left:493px;top:2552px">
  <svg width="14" height="18" viewBox="0 0 14 18"><path d="M7 1a6 6 0 0 1 6 6c0 4-6 10-6 10S1 11 1 7a6 6 0 0 1 6-6z" fill="var(--green)"/><circle cx="7" cy="7" r="2" fill="#fff"/></svg>
</div>
<p class="abs" style="left:543px;top:2548px;width:250px;font-size:18px;line-height:27px;color:#fff">1122 Duis aute irure dolor in reprehenderit in voluptate velit esse</p>
<div class="abs contact-ico" style="left:495px;top:2638px">
  <svg width="18" height="13" viewBox="0 0 18 13"><rect x="1" y="1" width="16" height="11" rx="1" fill="none" stroke="var(--green)" stroke-width="1.6"/><path d="M1 1l8 6 8-6" fill="none" stroke="var(--green)" stroke-width="1.6"/></svg>
</div>
<p class="abs serif" style="left:543px;top:2643px;font-size:18px;color:#fff">+1 888 888 8888</p>

<h3 class="abs f-head serif" style="left:886px;color:#fff">Quick Links</h3>
<div class="abs links" style="color:#fff">Home<br>About Us<br>Products<br>Gallery<br>Contact Us</div>

<p class="abs copy serif" style="color:#fff">© copyrights 2022 &nbsp;Bikeshop Valdorna | &nbsp;All Rights Reserved</p>

</body>
</html>
```